Coastal Rubdown Oil Co. needs a new label.

This massage oil has been in Australia for over 20 years and needs a new label for its plastic 250ml bottles. The current label (8cm x 8cm) looks old fashioned and so we are looking for something that reflects freedom, relaxation, inspiration. The product is made from sweet almond oil and has different essential oils used to give unique smells. I have seen some lovely abstract vector images. I think we need a clean straight look with bright colours. There are currently six variations to the product. "Weary and Worn Heads, Achy and Spent Frames, Couples Mix, Heather Soak Oil, Unwinding Mix, Uplift Mix" Different coloured labels have been used for each of the blends. I have included photos of existing bottles plus some ideas for the labels.

I would like to use the same font on the name of the brand Bramblewick Acres. If we change the font it may be difficult for existing customers to find our product.

Also just under the name Bramblewick Acres I would like to insert a type of logo (can be the shape of a tear drop or round circle) to say:

Massage Oil
Since 1970

The size of the label is 8cm x 12 cm for the front and the same size for the back of the label.
Updates

Coastal Rubdown oil Company has posted on the brief some images from Pixelvault plus two photos of the original bottles. I am looking for a new design which is bright in colour, fun and funky. I am not thinking along the lines of the traditional Herb and trees look. I think the original label is too busy and the colours overpower the label. The other point I think that is important is that the product has been around since 1970. If there is room I think a round logo which says: Massage Oil Since 1970 I am hoping that we can fit this information on the label Looking forward to seeing all the designs come thru. So far I have only had two designs come thru. Speak soon from hot sunny Australia. maree

Thank you to everyone who has already posted designs for our Massage Label. I have now edited the brief to include some more ideas on how to make this design the Best! I will email back to you straight away ideas and thoughts on your designs. Remember I live in Australia and can be either 10hrs in front or behind your time.

Reason: Due to busy lives and commitments over the next few days I feel that an extension will benefit all involved. Thank you to everyone who has submitted designs and working with me to create something beautiful. maree

Hello from Australia all the designers who have submitted some wonderful designs over the past two weeks. We are now entering the final three days of the competition. Thank you to everyone who has worked so hard to try and create the perfect label for my massage oil bottle. All of you have done a fantastic job. This has made the decision hard to make. Thank you to everyone. Please submit all your last minute designs soon. kind regards maree Australia

Target Market(s)

The type of person purchasing a massage oil blend will buy from a health food shop, pharmacy or from an on-line store. I believe they are wanting something bright that clearly communicates that that it is a massage oil.

Industry/Entity Type

Massage

Font styles to use
Script

Requirements
Must have
• Different colour for each massage oil blend.
Need same font for the name Bramblewick Acres. (script font or similar)

Abstract design please.
Nice to have
• A logo under the name Bramblewick Acres

Tear Drop or circle design that says:

Massage Oil
Since 1970

also we would like an outline for the back label. (see photo attached)

BACK LABEL information

A unique blend of essential oils in a fine light base.

Contains:

vegetable oil extract of nettle, sweet almond oil, ethanol, essential oils of lavender, lemongrass, orange & ylang ylang and vitamin E.

How to Use:

Shake well warm bottle in warm water if very cold.
Lovingly massage the body from head to toe.
Not for medicinal use.

Bramblewick Acres
Hollin WA 6099
Phone: (08) 9555 0142

(LEAVE ROOM FOR BARCODE)
Should not have
• Too busy design or old fashioned design.
No dull colours.

```html
<!DOCTYPE html>
<html lang="en">
<head>
<meta charset="utf-8">
<title>Bramblewick Acres – Massage Oil Label</title>
<link rel="stylesheet" href="https://fonts.googleapis.com/css2?family=Great+Vibes&family=Montserrat:wght@500;600;700&family=Questrial&display=swap">
<style>
  :root {
    --backdrop: #ececec;
    --crimson: #a42a48;
    --crimson-soft: #b6496a;
    --cream: #f7efbd;
    --cream-faint: rgba(247, 239, 189, 0.35);
  }
  * { margin: 0; padding: 0; box-sizing: border-box; }
  html, body {
    width: 857px; height: 1200px; overflow: hidden;
    background: var(--backdrop);
  }
  .label {
    position: absolute; left: 67px; top: 57px;
    width: 725px; height: 1086px;
    background: var(--crimson);
    border-radius: 24px;
    overflow: hidden;
    box-shadow: 0 2px 10px rgba(0,0,0,0.18);
    color: var(--cream);
  }
  .pattern { position: absolute; }
  .pattern-top {
    left: 0; top: 0; width: 600px; height: 150px;
    background: radial-gradient(ellipse at 40% 0%, var(--cream-faint), rgba(247,239,189,0) 70%);
  }
  .pattern-left {
    left: 0; top: 0; width: 190px; height: 660px;
    background: radial-gradient(ellipse at 0% 35%, var(--cream-faint), rgba(247,239,189,0) 72%);
  }
  .pattern-bottom {
    left: 0; bottom: 0; width: 725px; height: 160px;
    background: linear-gradient(to bottom, rgba(247,239,189,0) 0%, rgba(247,239,189,0.55) 55%, rgba(247,239,189,0.7) 100%);
  }
  .volume-tab {
    position: absolute; right: 0; top: 85px;
    width: 64px; height: 148px;
    background: var(--cream);
    border-radius: 12px 0 0 12px;
    display: flex; align-items: center; justify-content: center;
  }
  .volume-tab span {
    transform: rotate(-90deg);
    white-space: nowrap;
    font-family: "Montserrat", sans-serif; font-weight: 500;
    font-size: 34px; color: var(--crimson);
  }
  .seal {
    position: absolute; left: 0; width: 725px; top: 228px;
    display: flex; align-items: center; justify-content: center; gap: 12px;
    font-family: "Montserrat", sans-serif; font-weight: 600;
    font-size: 15px; letter-spacing: 2px; text-transform: uppercase;
  }
  .seal-dot {
    width: 20px; height: 20px; border-radius: 50%; background: var(--cream);
  }
  .brand-name {
    position: absolute; left: 0; width: 725px; top: 265px;
    font-family: "Great Vibes", cursive; font-weight: 400;
    line-height: 1;
  }
  .brand-name .line-one { display: block; font-size: 128px; padding-left: 70px; }
  .brand-name .line-two { display: block; font-size: 140px; padding-left: 250px; margin-top: -18px; }
  .product {
    position: absolute; left: 0; width: 725px; top: 645px;
    text-align: center;
    font-family: "Montserrat", sans-serif; font-weight: 600;
    text-transform: uppercase;
  }
  .product .lead { display: block; font-size: 35px; line-height: 44px; }
  .product .blend { display: block; font-size: 44px; line-height: 54px; font-weight: 500; }
  .description {
    position: absolute; left: 58px; width: 608px; top: 762px;
    font-family: "Questrial", sans-serif; font-size: 16.4px; line-height: 22.2px;
    text-align: justify; text-align-last: center;
  }
  .tagline {
    position: absolute; left: 113px; top: 883px;
    width: 495px; height: 33px;
    background: var(--cream); color: var(--crimson);
    border-radius: 6px;
    display: flex; align-items: center; justify-content: center;
    font-family: "Montserrat", sans-serif; font-weight: 700;
    font-size: 15px; letter-spacing: 2.6px; text-transform: uppercase;
  }
</style>
</head>
<body>
  <main class="label">
    <div class="pattern pattern-top" role="img" aria-label="Cream line-drawn flower and leaf pattern along the top edge"></div>
    <div class="pattern pattern-left" role="img" aria-label="Cream outlined floral blooms along the left edge"></div>
    <div class="pattern pattern-bottom" role="img" aria-label="Band of cream leaf and petal shapes along the bottom edge"></div>

    <div class="volume-tab"><span>250 ml</span></div>

    <div class="seal"><span class="seal-dot"></span><span>Massage Oil · Since 1970</span></div>

    <h1 class="brand-name">
      <span class="line-one">Bramblewick</span>
      <span class="line-two">Acres</span>
    </h1>

    <h2 class="product">
      <span class="lead">Massage oil for</span>
      <span class="blend">Weary &amp; Worn Heads</span>
    </h2>

    <p class="description">Lorem ipsum dolor sit amet, consectetur adipisicing elit, sed do eiusmod tempor incididunt ut labore et dolore magna aliqua. Ut enim ad minim veniam, quis nostrud exercitation. Lorem ipsum dolor sit amet, consectetur adipisicing elit, sed do eiusmod tempor incididunt ut labore et dolore magna aliqua.</p>

    <div class="tagline">Twenty years of natural skin care</div>
  </main>
</body>
</html>
```